MEDICAL CLINIC LETTERHEAD

Design is a letterhead for a non-profit medical center. The name of the clinic is VITORRANE Community Health Center. Although the full name must be included, the community health center part is more of a description and should be less visible - i attached an example of what I mean by that (ATTACHED IMAGE IS AN EXAMPLE OF FONT SIZES NOT A DESIGN IDEA). Please design something modern, cool looking and unique because I can always download free templates.
Phone, email, website and etc will be added later.

Industry/Entity Type

MEDICAL

```html
<!DOCTYPE html>
<html lang="en">
<head>
<meta charset="utf-8">
<title>VITORRANE Community Health Center – Letterhead</title>
<link rel="stylesheet" href="https://fonts.googleapis.com/css2?family=Montserrat:wght@400;600;700&family=Raleway:wght@300;400&family=Open+Sans:wght@600&display=swap">
<style>
  :root {
    --paper: #ffffff;
    --ink-dark: #4d4d4f;
    --ink-mid: #939598;
    --ink-body: #8a8c8f;
    --rule: #a7a9ac;
    --accent-orange: #f5a623;
    --accent-green: #1f8a3d;
    --accent-blue: #29a8e0;
  }
  * { margin: 0; padding: 0; box-sizing: border-box; }
  html, body { width: 908px; height: 1200px; overflow: hidden; background: var(--paper); }
  .letterhead {
    position: relative;
    width: 908px;
    height: 1200px;
    background: var(--paper);
    font-family: "Raleway", sans-serif;
    color: var(--ink-body);
  }
  .brand { position: absolute; left: 32px; top: 97px; width: 160px; }
  .brand-name {
    font-family: "Montserrat", sans-serif;
    font-weight: 700;
    font-size: 25px;
    line-height: 25px;
    letter-spacing: -0.6px;
    color: var(--ink-dark);
  }
  .brand-descriptor {
    font-family: "Montserrat", sans-serif;
    font-weight: 400;
    font-size: 8.4px;
    line-height: 10px;
    color: var(--ink-dark);
  }
  .header-rule {
    position: absolute;
    left: 199px; top: 124px;
    width: 502px; height: 1px;
    background: var(--rule);
  }
  .org-contact { position: absolute; left: 711px; top: 69px; list-style: none; }
  .org-contact li {
    display: flex; align-items: center; gap: 5px;
    height: 22px;
    font-family: "Montserrat", sans-serif;
    font-size: 12.4px;
    color: var(--ink-dark);
  }
  .org-contact svg { width: 11px; height: 11px; flex: none; }
  .recipient { position: absolute; left: 41px; top: 236px; font-family: "Montserrat", sans-serif; color: var(--ink-mid); }
  .recipient-name { font-weight: 600; font-size: 26px; line-height: 34px; letter-spacing: 0.4px; }
  .recipient-line { font-size: 14.5px; line-height: 20px; margin-top: 6px; }
  .recipient-address { font-size: 14.5px; line-height: 20px; margin-top: 7px; }
  .letter-date {
    position: absolute; right: 43px; top: 345px;
    font-family: "Open Sans", sans-serif; font-weight: 600;
    font-size: 17px; color: var(--ink-mid);
  }
  .letter-body { position: absolute; left: 36px; width: 829px; }
  .letter-body p {
    font-weight: 300; font-size: 16.6px; line-height: 19.7px;
    text-align: justify; hyphens: auto; color: var(--ink-body);
  }
  .body-one { top: 402px; }
  .body-two { top: 540px; }
  .body-three { top: 678px; }
  .sign-off {
    position: absolute; left: 66px; top: 832px;
    font-weight: 300; font-size: 18.5px; color: var(--ink-mid);
  }
  .signature {
    position: absolute; left: 86px; top: 880px;
    width: 166px; height: 100px;
    background: linear-gradient(135deg, #f4f4f5, #e9e9ea);
    border-radius: 4px;
  }
</style>
</head>
<body>
<main class="letterhead">
  <header>
    <div class="brand">
      <div class="brand-name">VITORRANE</div>
      <div class="brand-descriptor">COMMUNITY HEALTH CENTER</div>
    </div>
    <div class="header-rule"></div>
    <ul class="org-contact">
      <li>
        <svg viewBox="0 0 12 12" aria-hidden="true"><circle cx="6" cy="6" r="6" fill="var(--accent-orange)"/><path d="M4 3.2l1 1.4-.6.7a4 4 0 0 0 2.3 2.3l.7-.6 1.4 1-.6 1A5 5 0 0 1 3 4l1-.8z" fill="#fff"/></svg>
        0155-820-347
      </li>
      <li>
        <svg viewBox="0 0 12 12" aria-hidden="true"><circle cx="6" cy="6" r="6" fill="var(--accent-green)"/><rect x="3" y="4" width="6" height="4.2" fill="#fff"/><path d="M3 4l3 2.3L9 4" fill="none" stroke="var(--accent-green)" stroke-width="0.8"/></svg>
        info@vitorrane.org
      </li>
      <li>
        <svg viewBox="0 0 12 12" aria-hidden="true"><circle cx="6" cy="6" r="6" fill="var(--accent-blue)"/><g fill="none" stroke="#fff" stroke-width="0.7"><circle cx="6" cy="6" r="3.4"/><ellipse cx="6" cy="6" rx="1.5" ry="3.4"/><path d="M2.6 6h6.8"/></g></svg>
        www.vitorrane.org
      </li>
    </ul>
  </header>

  <section class="recipient">
    <div class="recipient-name">MARA ELLISON</div>
    <div class="recipient-line">0155-820-347</div>
    <div class="recipient-line">info@ellisonmail.com</div>
    <div class="recipient-address">4821 Meadowbrook Ave. Suite<br>210 Fairview, TX 0000</div>
  </section>

  <div class="letter-date">12 December, 2023</div>

  <div class="letter-body body-one">
    <p>Lorem ipsum dolor sit amet, consectetuer adipiscing elit, sed diam nonummy nibh euismod tincidunt ut laoreet dolore magna aliquam erat volutpat. Ut wisi enim ad minim veniam, quis nostrud exerci tation ullamcorper suscipit lobortis nisl ut aliquip ex ea commodo consequat. Duis autem vel eum iriure dolor in hendrerit in vulputate velit esse molestie consequat, vel illum dolore eu feugiat nulla facilisis at vero eros et accumsan et iusto odio dignissim qui blandit praesent luptatum zzril delenit augue duis dolore te feugait nulla facilisi.</p>
  </div>
  <div class="letter-body body-two">
    <p>Lorem ipsum dolor sit amet, cons ectetuer adipiscing elit, sed diam nonummy nibh euismod tincidunt ut laoreet dolore magna aliquam erat volutpat. Ut wisi enim ad minim veniam, quis nostrud exerci tation ullamcorper suscipit lobortis nisl ut aliquip ex ea commodo consequat.</p>
    <p>Lorem ipsum dolor sit amet, consectetuer adipiscing elit, sed diam nonummy nibh euismod tincidunt ut laoreet dolore magna aliquam erat</p>
  </div>
  <div class="letter-body body-three">
    <p>Lorem ipsum dolor sit amet, cons ectetuer adipiscing elit, sed diam nonummy nibh euismod tincidunt ut laoreet dolore magna aliquam erat volutpat. Ut wisi enim ad minim veniam, quis nostrud exerci tation ullamcorper suscipit lobortis nisl ut aliquip ex ea commodo consequat. Lorem ipsum dolor sit zamet, consectetuer adipiscing elit, sed diam nonummy nibh euismod tincidunt.</p>
  </div>

  <div class="sign-off">Managing Director</div>
  <div class="signature" role="img" aria-label="Handwritten signature of the managing director"></div>
</main>
</body>
</html>
```